business cards for heating company

I need business cards for my heating air conditioning and chimney company located in upstate NY I would like for them to be colorful and catchy on heavy stock with preferably a glossy finish on front of card but the ability to write something on one half of the back with maybe some bullets on the other half of the back I also need to be able to change the name and title of employees on the card and also incorporate some of our current look and feel from our trucks and website I also want to be able to use this design or similar to have door hangers made lawn signs coffee mugs key chains etc. our website is Brindlecove.com

Target Market(s)

homeowners

Industry/Entity Type

Air Conditioning

Contact Information for Business Card

should have website brindlecove.com , phone number 585-437-9184 please look at website for ideas

Font styles to use
Sans Serif

Colors
ec1f27
3176b5
fbee3f

Requirements
Must have
• a complete look
Nice to have
• a discount offer like 10% military and first responders
• senior discount %5

```html
<!DOCTYPE html>
<html lang="en">
<head>
<meta charset="utf-8">
<title>Brindle Cove – Business Card</title>
<link rel="stylesheet" href="https://fonts.googleapis.com/css2?family=Lato:wght@400;700;900&display=swap">
<style>
  :root{
    --backdrop:#e9e6e1;
    --card:#ffffff;
    --card-shade:#f1f1f1;
    --rose:#c9416a;
    --rose-deep:#b03358;
    --blue:#1f72b6;
    --blue-deep:#165f9c;
    --ink:#4a4a4a;
    --ink-soft:#6d6d6d;
    --rule:#d2587c;
  }
  *{box-sizing:border-box;margin:0;padding:0}
  html,body{width:1200px;height:600px;overflow:hidden}
  body{
    background:var(--backdrop);
    font-family:"Lato",Arial,sans-serif;
    display:flex;align-items:center;justify-content:center;gap:60px;
  }
  .card{
    width:520px;height:297px;position:relative;overflow:hidden;
    background:linear-gradient(160deg,var(--card) 55%,var(--card-shade));
    box-shadow:0 10px 28px rgba(0,0,0,.18);
  }

  /* Front */
  .front .person{position:absolute;left:40px;top:34px}
  .front .name{color:var(--blue);font-weight:700;font-size:19px}
  .front .title{color:var(--ink-soft);font-size:12px;margin-top:3px}
  .front .address{position:absolute;left:40px;top:104px;color:var(--ink);font-size:12.5px;line-height:1.5}
  .front .contact{position:absolute;left:40px;top:158px;list-style:none;color:var(--ink);font-size:12.5px;line-height:1.6}
  .front .contact li{display:flex;align-items:center;gap:7px}
  .front .contact svg{width:12px;height:12px;flex:none}
  .front .band{
    position:absolute;left:0;right:0;bottom:0;height:58px;background:var(--rose);
    display:flex;flex-direction:column;justify-content:center;padding-left:40px;
  }
  .front .band::before{content:"";position:absolute;left:0;right:0;top:-5px;height:5px;background:var(--blue)}

  .brand{color:#fff;font-weight:900;font-size:22px;letter-spacing:1px;text-transform:uppercase;line-height:1}
  .tagline{color:#fff;font-size:11px;letter-spacing:1.2px;text-transform:uppercase;margin-top:4px}

  /* Back */
  .back .header{
    position:absolute;left:0;right:0;top:0;height:40px;background:var(--blue);
    color:#fff;font-weight:700;font-size:15px;display:flex;align-items:center;padding-left:26px;
  }
  .back .slots{position:absolute;left:26px;right:26px;top:62px;list-style:none}
  .back .slot{display:flex;gap:22px;margin-bottom:22px;font-size:12px;color:var(--blue)}
  .back .field{display:flex;align-items:flex-end;gap:6px}
  .back .field.date{flex:1.4}
  .back .field.time{flex:1}
  .back .line{flex:1;border-bottom:1px solid var(--rule);height:12px}
  .back .notice{
    position:absolute;left:0;right:0;bottom:58px;height:24px;background:var(--blue);
    color:#fff;font-size:11px;display:flex;align-items:center;padding-left:26px;
  }
  .back .band{
    position:absolute;left:0;right:0;bottom:0;height:58px;background:var(--rose);
    display:flex;align-items:center;justify-content:space-between;padding:0 26px;
  }
  .back .band .brand{font-size:20px}
  .back .web{color:#fff;font-size:12px;letter-spacing:.5px}
</style>
</head>
<body>

  <section class="card front" aria-label="Business card front">
    <div class="person">
      <p class="name">Daniel Hargrove</p>
      <p class="title">Managing Director</p>
    </div>
    <p class="address">1187 Maple Hill Road<br>Webster, NY 14580</p>
    <ul class="contact">
      <li>
        <svg viewBox="0 0 12 12" aria-hidden="true"><rect width="12" height="12" rx="2" fill="var(--blue)"/><path d="M3.5 2.8l1.4-.4.8 1.8-.9.7c.4.9 1 1.5 1.9 1.9l.7-.9 1.8.8-.4 1.4C6.2 8.9 3.1 5.8 3.5 2.8z" fill="#fff"/></svg>
        (585) 437-9184
      </li>
      <li>
        <svg viewBox="0 0 12 12" aria-hidden="true"><rect width="12" height="12" rx="2" fill="var(--blue)"/><rect x="2.5" y="3.5" width="7" height="5" fill="none" stroke="#fff" stroke-width="1"/><path d="M2.5 3.5L6 6.3l3.5-2.8" fill="none" stroke="#fff" stroke-width="1"/></svg>
        info@brindlecove.com
      </li>
      <li>
        <svg viewBox="0 0 12 12" aria-hidden="true"><circle cx="6" cy="6" r="6" fill="var(--blue)"/><circle cx="6" cy="6" r="3.8" fill="none" stroke="#fff" stroke-width=".9"/><path d="M2.2 6h7.6M6 2.2c-1.6 2.4-1.6 5.2 0 7.6M6 2.2c1.6 2.4 1.6 5.2 0 7.6" fill="none" stroke="#fff" stroke-width=".8"/></svg>
        brindlecove.com
      </li>
    </ul>
    <div class="band">
      <p class="brand">Brindle Cove</p>
      <p class="tagline">Heating, Cooling &amp; Chimney</p>
    </div>
  </section>

  <section class="card back" aria-label="Business card back">
    <h2 class="header">Next Appointment</h2>
    <ul class="slots">
      <li class="slot"><span class="field date">Date :<span class="line"></span></span><span class="field time">Time :<span class="line"></span></span></li>
      <li class="slot"><span class="field date">Date :<span class="line"></span></span><span class="field time">Time :<span class="line"></span></span></li>
      <li class="slot"><span class="field date">Date :<span class="line"></span></span><span class="field time">Time :<span class="line"></span></span></li>
    </ul>
    <p class="notice">Your appointment has been personally reserved for you. Late cancellation will usually incur a fee.</p>
    <div class="band">
      <div>
        <p class="brand">Brindle Cove</p>
        <p class="tagline">Heating, Cooling &amp; Chimney</p>
      </div>
      <p class="web">www.brindlecove.com</p>
    </div>
  </section>

</body>
</html>
```